Property Management Company Business Cards

Need business cards for a property management company located in Lakeport. We manage houses for clients all over the world. Young and modern company, looking for eye catching design. Please work with the attached logo.

Industry/Entity Type

Property Management

Requirements
Must have
• Need lines for address, telephone number, fax number, web site.

Also lines for name, and job title

```html
<!DOCTYPE html>
<html lang="en">
<head>
<meta charset="utf-8">
<title>Northvale Estates – Business Cards</title>
<link rel="stylesheet" href="https://fonts.googleapis.com/css2?family=Open+Sans:ital,wght@0,400;0,600;0,700;1,400;1,600;1,700&display=swap">
<style>
  :root {
    --ink: #252f38;
    --sky: #4fd6f7;
    --card-light: #f2f2f2;
    --card-mid: #d9d9d9;
    --card-edge: #c7c7c7;
    --paper: #ffffff;
    --white: #ffffff;
  }
  * { margin: 0; padding: 0; box-sizing: border-box; }
  html, body { width: 1200px; height: 1000px; overflow: hidden; background: var(--paper); }
  body { position: relative; font-family: "Open Sans", Arial, sans-serif; color: var(--ink); }

  .card {
    position: absolute;
    top: 326px;
    width: 532px;
    height: 343px;
    border-radius: 40px;
    overflow: hidden;
    background: radial-gradient(ellipse 60% 70% at 45% 45%, var(--card-light) 0%, var(--card-mid) 60%, var(--card-edge) 100%);
  }
  .card--front { left: 58px; }
  .card--back { left: 606px; }

  .brand { position: absolute; display: flex; align-items: center; white-space: nowrap; }
  .brand__dot { border-radius: 50%; background: var(--ink); flex: none; }
  .brand__name {
    color: var(--ink);
    font-weight: 700;
    line-height: 1;
    text-transform: uppercase;
    letter-spacing: -0.5px;
  }

  .card--front .brand { left: 68px; top: 129px; }
  .card--front .brand__dot { width: 62px; height: 62px; margin-right: 14px; }
  .card--front .brand__name { font-size: 33px; }

  .card--back .brand { left: 31px; top: 43px; }
  .card--back .brand__dot { width: 38px; height: 38px; margin-right: 9px; }
  .card--back .brand__name { font-size: 20px; }

  .tagline { position: absolute; left: 0; top: 251px; width: 532px; height: 31px; }
  .tagline__lead {
    position: absolute; left: 0; top: 0; width: 190px; height: 31px;
    background: var(--ink); color: var(--white);
    font-style: italic; font-weight: 700; font-size: 14px; letter-spacing: 1.8px;
    line-height: 31px; padding-left: 22px; white-space: nowrap;
  }
  .tagline__main {
    position: absolute; left: 174px; top: 0; right: 0; height: 31px;
    background: var(--sky); color: var(--white);
    border-left: 6px solid var(--card-light);
    border-radius: 16px 0 0 16px;
    font-size: 15px; letter-spacing: 1.9px; line-height: 31px; padding-left: 16px; white-space: nowrap;
  }
  .tagline__main strong { font-weight: 700; }

  .person { position: absolute; left: 0; top: 108px; width: 532px; height: 31px; }
  .person__name {
    position: absolute; left: 0; top: 0; width: 350px; height: 31px;
    background: var(--sky); color: var(--white);
    border-radius: 0 16px 16px 0;
    font-weight: 700; font-size: 17px; letter-spacing: 2.2px; line-height: 31px; padding-left: 31px;
    z-index: 2;
  }
  .person__role {
    position: absolute; left: 343px; top: 0; right: 0; height: 31px;
    background: var(--ink); color: var(--white);
    border-left: 6px solid var(--card-light);
    border-radius: 16px 0 0 16px;
    font-style: italic; font-weight: 600; font-size: 15px; letter-spacing: 1.2px; line-height: 31px; padding-left: 24px;
    z-index: 1;
  }

  .contact { position: absolute; left: 31px; font-style: italic; font-size: 13.5px; letter-spacing: 1px; line-height: 15.5px; }
  .contact--address { top: 180px; }
  .contact--lines { top: 248px; }
  .contact__accent { color: var(--sky); font-weight: 600; }

  .mark-circle {
    position: absolute; left: 357px; top: 180px; width: 144px; height: 144px;
    border-radius: 50%; background: var(--ink); opacity: 0.9;
  }
</style>
</head>
<body>

  <section class="card card--front" aria-label="Business card front">
    <div class="brand">
      <span class="brand__dot"></span>
      <span class="brand__name">Northvale Estates</span>
    </div>
    <div class="tagline">
      <div class="tagline__lead">CHOOSE THE BEST</div>
      <div class="tagline__main">PROPERTY MANAGEMENT <strong>COMPANY</strong></div>
    </div>
  </section>

  <section class="card card--back" aria-label="Business card back">
    <div class="brand">
      <span class="brand__dot"></span>
      <span class="brand__name">Northvale Estates</span>
    </div>
    <div class="person">
      <div class="person__name">NAME NAME</div>
      <div class="person__role">Manager</div>
    </div>
    <p class="contact contact--address">address<br><span class="contact__accent">Lakeport</span></p>
    <p class="contact contact--lines">tel. 31827406<br>fax. 472930618<br><span class="contact__accent">www.northvaleestates.com</span></p>
    <span class="mark-circle"></span>
  </section>

</body>
</html>
```